Tarvoe Aviation Consultants Business card

I need a business card design for a new aviation company called Tarvoe Aviation Consultants. Our focus is on large airplane end-of-life solutions. This is typically where an airline retires an aircraft and we would oversee the dismantling of the aircraft into the valuable components and parts. The removed parts are then overhauled and reintroduced into the market place.
'Tarvoe' means 'island in the clouds'. I envision an airplane flying into the sunset as it's days are numbered. I am also very keen on our Florida island vibe.
Industry/Entity Type
Aviation
Contact Information for Business Card
Tarvoe Aviation Consultants
End of Life Specialists
Glen Morsk - President
418 SW 27th Ave
Fort Lauderdale, FL 33872
+1 954 555-0183
Logo Text
Requirements
Must have
- airplane
Nice to have
- sunset
- somewhere on the card it would be the definition of 'Tarvoe' - island in the clouds

```html
<!DOCTYPE html>
<html lang="en">
<head>
<meta charset="utf-8">
<title>Tarvoe Aviation Consultants – Business Card</title>
<link rel="stylesheet" href="https://fonts.googleapis.com/css2?family=Oswald:wght@500;600&family=Exo+2:ital,wght@1,500&display=swap">
<style>
  :root {
    --red: #f0241b;
    --orange: #ff5612;
    --black: #050505;
    --rail: #3a3a3a;
    --pale: #ecebea;
    --sky-top: #8b6f86;
    --sky-mid: #e9864a;
    --sea: #a8391f;
    --placeholder-grey: #bdbdbd;
  }
  * { margin: 0; padding: 0; box-sizing: border-box; }
  html, body { width: 1200px; height: 1200px; overflow: hidden; background: #fff; }
  .canvas { position: relative; width: 1200px; height: 1200px; }

  .card {
    position: absolute;
    left: 200px;
    width: 798px;
    height: 452px;
    background: #fff;
    overflow: hidden;
    box-shadow: 0 22px 18px -14px rgba(0,0,0,.55);
  }
  .card--front { top: 112px; }
  .card--back { top: 660px; border: 1px solid #777; }

  .card__shapes { position: absolute; inset: 0; }

  .front__title {
    position: absolute;
    left: 0; top: 106px;
    width: 400px; height: 50px;
    display: flex; align-items: center; justify-content: center;
    font-family: "Oswald", sans-serif;
    font-weight: 600;
    font-size: 34px;
    letter-spacing: -0.5px;
    color: #fff;
    transform: scaleY(1.1);
  }
  .front__details {
    position: absolute;
    left: 38px; top: 190px;
    list-style: none;
  }
  .front__details li {
    display: flex; align-items: center;
    height: 46.3px;
    font-family: "Exo 2", sans-serif;
    font-style: italic;
    font-weight: 500;
    font-size: 27px;
    color: var(--red);
  }
  .front__details .bullet { width: 20px; height: 20px; margin-right: 6px; flex: none; }

  .back__title {
    position: absolute;
    left: 0; right: 0; top: 80px;
    text-align: center;
    font-family: "Oswald", sans-serif;
    font-weight: 600;
    font-size: 46px;
    letter-spacing: -1px;
    color: var(--orange);
  }
  .back__footer {
    position: absolute;
    left: 0; right: 0; top: 398px; height: 54px;
    background: var(--orange);
    border-top: 12px solid var(--black);
    display: flex; align-items: center; justify-content: center;
    font-family: "Oswald", sans-serif;
    font-weight: 500;
    font-size: 17.5px;
    color: #fff;
    white-space: nowrap;
    letter-spacing: -0.2px;
  }
  .back__illustration {
    position: absolute;
    left: 283px; top: 216px;
    width: 236px; height: 88px;
    background: linear-gradient(180deg, #fff 0 55%, var(--placeholder-grey) 55% 100%);
    border: 1px solid #888;
  }
</style>
</head>
<body>
<main class="canvas">

  <section class="card card--front" aria-label="Card front">
    <svg class="card__shapes" viewBox="0 0 798 452" width="798" height="452">
      <defs>
        <linearGradient id="sunset" x1="0" y1="0" x2="0" y2="1">
          <stop offset="0" stop-color="var(--sky-top)"/>
          <stop offset="0.45" stop-color="var(--sky-mid)"/>
          <stop offset="0.62" stop-color="#f2a15a"/>
          <stop offset="0.75" stop-color="var(--sea)"/>
          <stop offset="1" stop-color="#5a1f14"/>
        </linearGradient>
        <symbol id="plane" viewBox="0 0 24 24">
          <path d="M1 10.5h8L5 2h3.2l7 8.5h5.3a1.5 1.5 0 0 1 0 3h-5.3l-7 8.5H5l4-8.5H1z"/>
        </symbol>
      </defs>

      <rect class="left-bar" x="0" y="0" width="30" height="452" fill="var(--black)"/>
      <polygon class="pale-wedge" points="236,0 328,0 544,244 520,230" fill="var(--pale)"/>
      <polygon class="chevron-band" points="328,0 400,0 560,250 360,452 304,452 544,244" fill="var(--black)"/>
      <polygon class="sunset-photo" role="img"
               aria-label="Photo: airliner flying into a tropical sunset over the sea with palm silhouette"
               points="400,0 798,0 798,452 360,452 560,250" fill="url(#sunset)"/>

      <rect class="title-band" x="0" y="106" width="400" height="50" fill="var(--red)"/>
      <rect x="0" y="158" width="400" height="2" fill="var(--red)"/>
      <rect x="0" y="162" width="400" height="2" fill="var(--red)"/>
      <rect x="404" y="106" width="6" height="62" fill="var(--red)"/>
      <rect x="414" y="106" width="6" height="62" fill="#ff6a4a"/>
      <rect x="424" y="106" width="4" height="62" fill="#ddd"/>
      <use href="#plane" x="430" y="108" width="60" height="60" fill="var(--orange)"/>
      <polygon points="4,166 30,166 30,204" fill="#8a1a12"/>
    </svg>

    <div class="front__title">Tarvoe Aviation Consultants</div>

    <ul class="front__details">
      <li><svg class="bullet" viewBox="0 0 20 20"><circle cx="10" cy="10" r="10" fill="var(--red)"/><path d="M6 10h8M10 6l4 4-4 4" stroke="#fff" stroke-width="2" fill="none"/></svg>End of Life Specialists</li>
      <li><svg class="bullet" viewBox="0 0 20 20"><circle cx="10" cy="10" r="10" fill="var(--red)"/><path d="M6 10h8M10 6l4 4-4 4" stroke="#fff" stroke-width="2" fill="none"/></svg>Glen Morsk - President</li>
      <li><svg class="bullet" viewBox="0 0 20 20"><circle cx="10" cy="10" r="10" fill="var(--red)"/><path d="M6 10h8M10 6l4 4-4 4" stroke="#fff" stroke-width="2" fill="none"/></svg>418 SW 27th Ave</li>
      <li><svg class="bullet" viewBox="0 0 20 20"><circle cx="10" cy="10" r="10" fill="var(--red)"/><path d="M6 10h8M10 6l4 4-4 4" stroke="#fff" stroke-width="2" fill="none"/></svg>Fort Lauderdale, FL 33872</li>
      <li><svg class="bullet" viewBox="0 0 20 20"><circle cx="10" cy="10" r="10" fill="var(--red)"/><path d="M6 10h8M10 6l4 4-4 4" stroke="#fff" stroke-width="2" fill="none"/></svg>+1 954 555-0183</li>
    </ul>
  </section>

  <section class="card card--back" aria-label="Card back">
    <svg class="card__shapes" viewBox="0 0 798 452" width="798" height="452">
      <defs>
        <symbol id="plane-b" viewBox="0 0 24 24">
          <path d="M1 10.5h8L5 2h3.2l7 8.5h5.3a1.5 1.5 0 0 1 0 3h-5.3l-7 8.5H5l4-8.5H1z"/>
        </symbol>
      </defs>
      <rect class="runway-line" x="0" y="152" width="798" height="8" fill="var(--rail)"/>
      <g fill="var(--orange)">
        <use href="#plane-b" x="-100" y="134" width="46" height="46" transform="scale(-1,1)"/>
        <use href="#plane-b" x="-348" y="134" width="46" height="46" transform="scale(-1,1)"/>
        <use href="#plane-b" x="442" y="134" width="46" height="46"/>
        <use href="#plane-b" x="660" y="134" width="46" height="46"/>
      </g>
    </svg>

    <div class="back__title">Tarvoe Aviation Consultants</div>
    <div class="back__illustration" role="img" aria-label="Illustration: excavator dismantling a retired airliner"></div>
    <div class="back__footer">End of Life Specialists, Glen Morsk - President, 418 SW 27th Ave, Fort Lauderdale, FL 33872, +1 954 555-0183</div>
  </section>

</main>
</body>
</html>
```